Business Card for Flag Company

Hello,

you should design a business card fitting to our company website:
http://www.tovbanners.de/

Information to print on the card:

My Name and Title:
Reinhold Brucker
Geschäftsführer / CEO

and the company data:

tovBanners GmbH
Am Lindenacker 14/3
71384 Lindhausen
Germany

My Phone number:
+49 7193 468 27 35

My Fax number:
+49 7193 468 27 80

My E-Mail:
brucker@tovBanners.de

Company domain:
www.tovBanners.de

I have attached the company logo and a company flyer to get an idea, what we like. Font of company logo.

Viable Dimensions Card: 85 x 55 mm
Needed file dimensions: 87 x 57mm

Thanks

Reinhold

Requirements
Must have
• Dimensions as described

```html
<!DOCTYPE html>
<html lang="de">
<head>
<meta charset="utf-8">
<title>tovBanners GmbH – Visitenkarte</title>
<link href="https://fonts.googleapis.com/css2?family=Arimo:wght@400;700&display=swap" rel="stylesheet">
<style>
  :root {
    --page: #ffffff;
    --photo-dark: #0c0d0f;
    --photo-mid: #2a2f34;
    --photo-light: #4a5157;
    --band-red: #e94b3c;
    --band-yellow: #f7b52c;
    --text-light: #ffffff;
    --text-warm: #fde3d6;
  }
  html, body {
    margin: 0;
    width: 1200px;
    height: 403px;
    overflow: hidden;
    background: var(--page);
    font-family: "Arimo", Arial, sans-serif;
  }
  .sheet {
    position: relative;
    width: 1200px;
    height: 403px;
  }
  .card {
    position: absolute;
    top: 15px;
    width: 572px;
    height: 373px;
    overflow: hidden;
    background: var(--photo-dark);
  }
  .card--front { left: 18px; }
  .card--back { left: 615px; }
  .card__photo {
    position: absolute;
    inset: 0;
  }
  .card--front .card__photo {
    background: radial-gradient(ellipse at 60% 40%, var(--photo-light) 0%, var(--photo-mid) 40%, var(--photo-dark) 80%);
  }
  .card--back .card__photo {
    background: radial-gradient(ellipse at 55% 60%, var(--photo-mid) 0%, #1a1d21 45%, var(--photo-dark) 80%);
  }
  .card__band {
    position: absolute;
    inset: 0;
    width: 572px;
    height: 373px;
  }
  .holder {
    position: absolute;
    right: 28px;
    bottom: 24px;
    text-align: right;
    color: var(--text-light);
  }
  .holder__name {
    font-size: 21px;
    font-weight: 400;
    letter-spacing: 0.4px;
    margin: 0 0 7px;
  }
  .holder__title {
    font-size: 13px;
    font-weight: 700;
    letter-spacing: 0.3px;
    margin: 0;
  }
  .contact {
    position: absolute;
    left: 48px;
    top: 270px;
    font-size: 11px;
    line-height: 13px;
    color: var(--text-warm);
  }
  .contact p { margin: 0; }
  .contact__row {
    display: flex;
  }
  .contact__row span:first-child {
    width: 127px;
  }
</style>
</head>
<body>
<div class="sheet">
  <section class="card card--front">
    <div class="card__photo" role="img" aria-label="Photo of a black car with a German flag mounted on a chrome pole at the side window"></div>
    <svg class="card__band" viewBox="0 0 572 373" aria-hidden="true">
      <path d="M0,232 C110,300 250,345 365,305 C455,274 515,228 572,226 L572,373 L0,373 Z" fill="var(--band-yellow)"/>
      <path d="M0,242 C110,310 250,355 365,315 C455,284 515,238 572,236 L572,373 L0,373 Z" fill="var(--band-red)"/>
    </svg>
    <div class="holder">
      <p class="holder__name">Reinhold Brucker</p>
      <p class="holder__title">Geschäftsführer / CEO</p>
    </div>
  </section>

  <section class="card card--back">
    <div class="card__photo" role="img" aria-label="Photo of a black car front with a European Union flag mounted on a chrome pole"></div>
    <svg class="card__band" viewBox="0 0 572 373" aria-hidden="true">
      <path d="M0,222 C110,222 200,280 300,300 C400,320 500,262 572,238 L572,373 L0,373 Z" fill="var(--band-yellow)"/>
      <path d="M0,232 C110,232 200,290 300,310 C400,330 500,272 572,248 L572,373 L0,373 Z" fill="var(--band-red)"/>
    </svg>
    <div class="contact">
      <p>tovBanners GmbH</p>
      <p>Am Lindenacker 14/3</p>
      <p>71384 Lindhausen</p>
      <p>Germany</p>
      <p class="contact__row"><span>PH+49 7193 468 27 35</span><span>FAX - 49 7193 468 27 80</span></p>
      <p class="contact__row"><span>brucker@tovBanners.de</span><span>www.tovBanners.de</span></p>
    </div>
  </section>
</div>
</body>
</html>
```